Fern Ledge Maplecrest Music Festival Poster

We are a summer music festival with concerts spanning Jazz, Cabaret, Education, Broadway, Chamber and Opera. We are looking for our key art for the 2016 season. This design will serve as the basis for all promotional materials, the concert program, and our web materials. Though eventually this means we will need to adjust the design to fit many different sizes, our poster will be printed mostly on 8.5" x 11" paper, and we can adapt from there. The design will be featured online and in print. It should be vertical and not landscape.

WE ARE SEEKING SLEEK, ELEGANT DESIGNS WITH MAYBE A KEY STOCK PHOTOGRAPH AND THE RELEVANT TEXT/DETAILS.

PLEASE NOTE: The included file "avenir logo.psd" is just a suggestion for the feel we are going for. It is our "working logo" after having scraped our old logo. We are interested in seeing your own ideas on how to style the brand name, but if you have ideas working with this version of the logo, feel free to use it.

REQUIRED DETAILS:
Festival Name: Fern Ledge Maplecrest Music Festival
Dates: July 29 - August 7 2016 (the year, 2016, must be included on the poster, but it does not need to be in the same location as where the actual dates are listed)
Website: www.fernledgemaplecrestfest.example

Additional Information:
- the 7 musical styles (jazz, choral, cabaret, education, broadway, chamber, opera) are important to defining who we are. You may decide to include these on the poster.
- We are looking for a very elegant design

TARGET:
We depend highly on an older clientele. We are working to expand our brand into younger demographics, but we want to be sure that we do not alienate our current consumer base with text that may be difficult for them to read.
Updates

Project Deadline Extended Reason: I am extending the deadline because it is taking longer to get feedback from my superiors than I had expected. Extending the deadline will give me time to provide adequate feedback from the people who will ultimately be making the decision. Thank you. Added Saturday, January 30, 2016

Sorry for the delay. There were issues with the decision makers but we are selecting in the next 24 hours.

Target Market(s)

Lovers of the styles of music we feature. We have a good number of elderly consumers, but also families and school groups (discussed further in description section)

Industry/Entity Type

Entertainment

Font styles to use
Sans Serif

Requirements
Must have
• Festival Name: Fern Ledge Maplecrest Music Festival
• Dates: July 29 - August 7 2016 (the year, 2016, must be included on the poster, but it does not need to be in the same location as where the actual dates are listed)
• Website: www.fernledgemaplecrestfest.example
Nice to have
• - the 7 musical styles (jazz, choral, cabaret, education, broadway, chamber, opera) are important to defining who we are. We would love to include these styles somewhere on the image, or feature them somehow in the artwork
• - Our brand has an elegance to it due to the type of music we offer, and our location being in a very natural space. inclusion of the music/nature mixed aspect of our brand in artwork might be nice
Should not have
• Anything that may offend or alienate an older, more conservative demographic

```html
<!DOCTYPE html>
<html lang="en">
<head>
<meta charset="utf-8">
<title>Fern Ledge Maplecrest Music Festival 2016</title>
<link rel="stylesheet" href="https://fonts.googleapis.com/css2?family=Oswald:wght@500&family=Raleway:wght@300;400&display=swap">
<style>
  :root {
    --night: #1d1d1d;
    --night-soft: #262626;
    --moon: #474747;
    --pine-dark: #3c5649;
    --pine-mid: #5d7e6e;
    --pine-mist: #86a797;
    --ground: #34473d;
    --rule: #8a8a8a;
    --text-light: #ececec;
    --text-muted: #d2d2d2;
    --date-gold: #f7f29a;
    --date-cream: #f5eed2;
  }
  * { margin: 0; padding: 0; box-sizing: border-box; }
  html, body {
    width: 860px; height: 1200px; overflow: hidden;
    background: var(--night);
  }
  .poster {
    position: relative; width: 860px; height: 1200px; overflow: hidden;
    background: linear-gradient(to bottom, var(--night) 0, var(--night-soft) 560px);
    font-family: "Raleway", sans-serif;
    color: var(--text-light);
  }
  .moon {
    position: absolute; left: 60px; top: 220px; width: 640px; height: 640px;
    border-radius: 50%;
    background: radial-gradient(circle at 50% 40%, #525252 0, var(--moon) 60%, #3a3a3a 100%);
  }
  .forest {
    position: absolute; left: 0; right: 0; top: 540px; bottom: 0;
    background: linear-gradient(to bottom,
      rgba(60,86,73,0) 0, var(--pine-dark) 60px,
      var(--pine-mid) 260px, var(--pine-mist) 480px,
      #769887 515px, var(--ground) 528px, var(--ground) 100%);
  }
  .tagline-band {
    position: absolute; left: 0; right: 0; top: 36px; height: 38px;
    border-top: 1px solid var(--rule);
    border-bottom: 1px solid var(--rule);
    display: flex; align-items: center; justify-content: center;
  }
  .tagline {
    font-size: 16px; font-weight: 400; letter-spacing: 0.42em;
    color: var(--text-muted); padding-left: 0.42em;
  }
  .genres {
    position: absolute; left: 0; right: 0; top: 104px;
    text-align: center; font-weight: 300; font-size: 35px;
    line-height: 41px; letter-spacing: 0.02em; color: var(--text-light);
    word-spacing: 0.45em;
  }
  .title {
    position: absolute; left: 0; right: 0; top: 268px; text-align: center;
    font-family: "Raleway", sans-serif; font-weight: 300;
    color: var(--text-light);
  }
  .title-line { display: block; }
  .title-line-1 { font-size: 78px; line-height: 86px; letter-spacing: 0.04em; }
  .title-line-2 { font-size: 90px; line-height: 100px; letter-spacing: 0.01em; }
  .title-line-3 { font-size: 50px; line-height: 80px; letter-spacing: 0.12em; margin-top: 6px; }
  .dates {
    position: absolute; left: 0; right: 0; top: 858px; text-align: center;
    font-family: "Oswald", sans-serif; font-weight: 500;
    color: var(--date-cream); line-height: 1;
  }
  .date-range { font-size: 56px; letter-spacing: 0.01em; }
  .date-range .day { font-size: 70px; color: var(--date-gold); }
  .date-year { display: block; font-size: 48px; margin-top: 10px; }
  .website {
    position: absolute; left: 0; right: 0; top: 1120px; text-align: center;
    font-size: 20px; letter-spacing: 0.34em; padding-left: 0.34em;
    color: var(--text-muted);
  }
</style>
</head>
<body>
  <main class="poster">
    <div class="moon" role="img" aria-label="Large full moon glowing in the night sky"></div>
    <div class="forest" role="img" aria-label="Misty pine forest silhouette in layered greens over a dark hillside"></div>

    <header class="tagline-band">
      <p class="tagline">IN THE MAJESTIC POCONO MOUNTAINS</p>
    </header>

    <p class="genres">JAZZ CHORAL CABARET OPERA<br>EDUCATION BROADWAY CHAMBER</p>

    <h1 class="title">
      <span class="title-line title-line-1">FERN LEDGE</span>
      <span class="title-line title-line-2">MAPLECREST</span>
      <span class="title-line title-line-3">MUSIC FESTIVAL</span>
    </h1>

    <p class="dates">
      <span class="date-range"><span class="day">29</span> JULY - <span class="day">7</span> AUGUST</span>
      <span class="date-year">2016</span>
    </p>

    <p class="website">WWW.FERNLEDGEMAPLECRESTFEST.EXAMPLE</p>
  </main>
</body>
</html>
```